Valmo Sàrl - Business Card

VALMO Sàrl operates in the sector Services for banks and credit institutions. It is a B2B which connects companies. The main colors should be Blue and Black. The logo and look of the card should be simple, professional, conservative and reflect Connecting People.

Target Market(s)

Financial professionals and institutions

Industry/Entity Type

Finance

Contact Information for Business Card

Chemin des Vergers 9
1048 Brenvaz

Logo Text

Linking Points

Font styles to use
Serif
Sans Serif

Colors
0355a3
3176b5
85acd3
cfdeed

Requirements
Should not have
• Multiple colors

```html
<!DOCTYPE html>
<html lang="fr">
<head>
<meta charset="utf-8">
<title>Valmo Sàrl – Business Card</title>
<link rel="stylesheet" href="https://fonts.googleapis.com/css2?family=Libre+Baskerville:wght@700&family=Mulish:wght@300;400&display=swap">
<style>
  :root {
    --backdrop: #b3b2ad;
    --paper: #ffffff;
    --ink: #111111;
    --blue-deep: #0355a3;
    --blue-mid: #3176b5;
    --blue-bright: #4ab2e6;
    --black-top: #2c2c2c;
    --black-bottom: #050505;
  }
  * { margin: 0; padding: 0; box-sizing: border-box; }
  html, body {
    width: 1200px;
    height: 1200px;
    overflow: hidden;
    background: var(--backdrop);
  }
  .stage {
    width: 1200px;
    height: 1200px;
    display: flex;
    align-items: center;
    justify-content: center;
  }
  .business-card {
    position: relative;
    width: 560px;
    height: 860px;
    background: var(--paper);
    box-shadow: 0 20px 50px rgba(0,0,0,0.25);
    overflow: hidden;
  }
  .card-art {
    position: absolute;
    inset: 0;
    width: 100%;
    height: 100%;
  }
  .brand {
    position: absolute;
    top: 300px;
    left: 0;
    right: 0;
    text-align: center;
  }
  .brand-name {
    font-family: "Libre Baskerville", serif;
    font-weight: 700;
    font-size: 54px;
    letter-spacing: 2px;
    color: var(--ink);
  }
  .brand-tagline {
    margin-top: 10px;
    font-family: "Mulish", sans-serif;
    font-weight: 400;
    font-size: 28px;
    letter-spacing: 3px;
    color: var(--blue-mid);
  }
  .address {
    position: absolute;
    left: 120px;
    bottom: 70px;
    display: flex;
    align-items: center;
    gap: 22px;
    color: #ffffff;
    font-family: "Mulish", sans-serif;
    font-style: normal;
    font-weight: 300;
    font-size: 26px;
    line-height: 1.25;
  }
  .pin-icon { width: 30px; height: 42px; flex: none; }
</style>
</head>
<body>
  <main class="stage">
    <article class="business-card">
      <svg class="card-art" viewBox="0 0 560 860" preserveAspectRatio="none" aria-hidden="true">
        <defs>
          <linearGradient id="band-deep" x1="0" y1="0" x2="1" y2="0">
            <stop offset="0" stop-color="#1d86c8"/>
            <stop offset="1" stop-color="#0355a3"/>
          </linearGradient>
          <linearGradient id="band-bright" x1="0" y1="0" x2="1" y2="0">
            <stop offset="0" stop-color="#4f9fd6"/>
            <stop offset="1" stop-color="#4ab2e6"/>
          </linearGradient>
          <linearGradient id="base-black" x1="0" y1="0" x2="0" y2="1">
            <stop offset="0" stop-color="#2c2c2c"/>
            <stop offset="1" stop-color="#050505"/>
          </linearGradient>
        </defs>
        <path d="M0 520 Q 260 640 560 430 L560 860 L0 860 Z" fill="url(#band-deep)"/>
        <path d="M0 565 Q 270 700 560 482 L560 860 L0 860 Z" fill="url(#band-bright)"/>
        <path d="M0 628 Q 280 748 560 532 L560 860 L0 860 Z" fill="#1c1c1c"/>
        <path d="M0 642 Q 280 765 560 548 L560 860 L0 860 Z" fill="url(#base-black)"/>
      </svg>

      <header class="brand">
        <h1 class="brand-name">VALMO Sàrl</h1>
        <p class="brand-tagline">LINKING POINTS</p>
      </header>

      <address class="address">
        <svg class="pin-icon" viewBox="0 0 30 42" aria-hidden="true">
          <path d="M15 0C6.7 0 0 6.5 0 14.6 0 25 15 42 15 42s15-17 15-27.4C30 6.5 23.3 0 15 0z" fill="#ffffff"/>
          <circle cx="15" cy="14.5" r="5.5" fill="#111111"/>
        </svg>
        <span>Chemin des Vergers 9<br>1048 Brenvaz</span>
      </address>
    </article>
  </main>
</body>
</html>
```